Website - Tides Of Bloom

We are catalysts of change in people's lives.
We work with individuals and professionals to bring about instant substantial & transforming change in their lives.
We provide one-on-one lifestyle coaching by an experienced practitioner.
Our existing website is www.tidesofbloom.biz & this site contains our the basis for the content of our desired new project, so please examine this carefully.
We require a professional and captivating website that will instantly impress, engage invite our readers to click & invest their lives.
Our services do not come cheap, but are second to none.
Our website must be contemporary whilst reflecting indisputable class & ultra-confidence in the success of our work.
Target Market(s)
Those who seek to want to change in their lives. Those aged primarily between 30 and 50 years of age, male or female.
Industry/Entity Type
Work
Look and feel

```html
<!DOCTYPE html>
<html lang="en">
<head>
<meta charset="utf-8">
<title>Tides Of Bloom — Life Coaching</title>
<link rel="stylesheet" href="https://fonts.googleapis.com/css2?family=Francois+One&family=Roboto+Condensed:wght@400;700&family=Raleway:wght@400;600&family=Open+Sans:ital,wght@0,400;0,600;1,400&display=swap">
<style>
:root{
  --black:#000;
  --ink:#111;
  --panel:#2b2b2b;
  --panel-dark:#1e1e1e;
  --grey-band:#cfcfcf;
  --light:#ececec;
  --white:#fff;
  --muted:#8a8a8a;
  --text-grey:#b9b9b9;
  --green:#5aa531;
  --accent-red:#c0121a;
  --link-red:#d42020;
  --blue-name:#2b6cb0;
  --head-font:"Roboto Condensed", Arial, sans-serif;
  --body-font:Arial, Helvetica, sans-serif;
}
*{box-sizing:border-box;margin:0;padding:0}
html,body{width:676px;height:1200px;overflow:hidden;background:var(--black)}
.page{position:relative;width:676px;height:1200px;overflow:hidden;font-family:var(--body-font);color:var(--white)}
.abs{position:absolute}

/* top bar */
.topbar{left:0;top:0;width:676px;height:16px;background:var(--black);font-size:7px}
.topbar .email{left:38px;top:4px;font-weight:bold}
.topbar .email span{color:var(--green);font-weight:normal}
.topbar .search{left:588px;top:0;width:22px;height:16px;background:#2a2a2a}
.topbar .lang{left:614px;top:4px;font-size:7px}

/* header */
.header{left:0;top:16px;width:676px;height:76px;background:linear-gradient(#3a3a3a,#1f1f1f)}
.header::after{content:"";position:absolute;left:0;top:0;width:676px;height:1px;background:#555}
.brand{left:38px;top:24px;width:180px;height:89px;background:linear-gradient(#111,#000);border:1px solid #444;box-shadow:0 2px 6px rgba(0,0,0,.8);z-index:3;display:flex;align-items:center;gap:8px;padding-left:16px}
.brand .mark{width:22px;height:22px;background:var(--green)}
.brand .name{font-family:var(--head-font);font-size:22px;line-height:1;color:var(--white);font-weight:400}
.social{top:30px;display:flex;gap:6px}
.social i{display:block;width:12px;height:12px;border-radius:50%;background:#ddd}
.social i.blue{background:#3b5998}
.nav{top:62px;left:428px;display:flex;gap:24px;font-family:"Open Sans",sans-serif;font-size:10px;font-weight:600;color:#ddd}
.nav .current{border-bottom:1px solid var(--accent-red);padding-bottom:3px}

/* hero */
.hero{left:0;top:92px;width:676px;height:237px;background:linear-gradient(90deg,#cfcfcf 0%,#efefef 40%,#fafafa 100%)}
.hero-photo{left:0;top:0;width:300px;height:237px;background:radial-gradient(ellipse at 45% 50%,#d9b8a0 0%,#c8b6a9 40%,#dcdcdc 75%,transparent 100%)}
.hero-callout{left:372px;top:59px;width:285px;height:118px;background:#3a3a3a;border-radius:40px 0 0 40px;box-shadow:0 3px 8px rgba(0,0,0,.5)}
.hero-callout h1{position:absolute;left:24px;top:28px;font-family:"Francois One",sans-serif;font-weight:400;font-size:31px;color:var(--green);letter-spacing:.3px}
.hero-callout p{position:absolute;left:24px;top:74px;font-family:"Open Sans",sans-serif;font-size:13px;color:var(--white)}
.hero-dots{left:594px;top:315px;display:flex;gap:5px}
.hero-dots i{width:8px;height:8px;border-radius:50%;background:#ddd;border:1px solid #999}
.hero-dots i.on{background:var(--green)}

/* band */
.band{left:0;top:329px;width:676px;height:12px;background:linear-gradient(#2a2a2a,#000)}
.section-bar{left:24px;top:344px;width:634px;height:23px;background:var(--white)}
.section-bar .tab{position:absolute;left:0;top:0;width:14px;height:23px;background:var(--accent-red)}
.section-bar .title{position:absolute;left:14px;top:0;width:412px;height:23px;background:var(--grey-band);clip-path:polygon(0 0,97% 0,100% 50%,97% 100%,0 100%);font-family:var(--head-font);font-weight:700;font-size:17px;line-height:23px;padding-left:6px;color:#222}
.section-bar .phone{position:absolute;right:22px;top:0;height:23px;display:flex;align-items:center;gap:6px;font-size:10px;color:#333}

/* services */
.services{left:24px;top:367px;width:634px;height:251px;display:flex;background:var(--black)}
.service{width:211px;padding:12px 18px 0 18px;position:relative}
.service + .service{border-left:1px dotted #555}
.service h3{display:flex;gap:6px;font-size:9.5px;line-height:10px;font-weight:bold;height:22px;align-items:flex-start}
.service h3 .bullet{flex:none;width:16px;height:16px;background:var(--green);margin-top:2px}
.service h3 span.txt{border-left:1px solid #888;padding-left:5px}
.service .photo{width:162px;height:104px;margin-top:2px}
.service p{margin-top:8px;font-size:8px;line-height:9px;color:#bbb;text-align:justify;font-weight:bold}
.service .more{position:absolute;right:24px;bottom:6px;font-size:8px;font-weight:bold}

/* quote banner */
.quote-banner{left:24px;top:626px;width:634px;height:25px;background:var(--grey-band);text-align:center;font-family:var(--head-font);font-weight:700;font-size:15px;line-height:25px;color:#1c1c1c;letter-spacing:.5px}
.quote-banner b{font-size:24px;vertical-align:-4px;font-family:Georgia,serif}
.quote-tip{left:310px;top:651px;width:0;height:0;border-left:16px solid transparent;border-right:16px solid transparent;border-top:15px solid var(--grey-band)}

/* feature area */
.features{left:24px;top:676px;width:634px;height:184px}
.feature{position:absolute;left:8px;width:270px;height:70px}
.feature .thumb{position:absolute;left:0;top:0;width:60px;height:36px}
.feature h4{position:absolute;left:76px;top:0;font-size:8.5px;font-weight:normal}
.feature p{position:absolute;left:76px;top:17px;font-size:8px;line-height:12px;font-weight:bold}
.feature .detail{position:absolute;right:0;top:40px;font-size:7.5px;color:var(--link-red)}
.feature-rule{left:32px;top:752px;width:264px;border-top:1px dotted #666}
.feature-divider{left:339px;top:680px;height:176px;border-left:1px solid #444}
.about{left:360px;top:679px;width:280px}
.about h2{font-family:var(--head-font);font-weight:400;font-size:12px;line-height:14px;letter-spacing:.2px}
.about p{font-size:7.5px;line-height:10px;font-weight:bold;margin-top:8px;letter-spacing:-.1px}
.about p:first-of-type{margin-top:7px}
.gallery{left:362px;top:810px;width:272px;display:flex;justify-content:space-between}
.gallery figure{width:80px;text-align:center}
.gallery .shot{width:80px;height:38px;border:1px solid #999}
.gallery figcaption{font-size:5.8px;margin-top:3px;line-height:7px}

/* testimonials */
.reviews{left:0;top:867px;width:676px;height:143px;background:var(--light)}
.reviews h2{position:absolute;left:0;top:8px;width:676px;text-align:center;font-family:Raleway,sans-serif;font-weight:400;font-size:15px;color:#555;letter-spacing:.2px}
.reviews h2 b{font-weight:600;color:#333}
.review{position:absolute;top:50px;width:318px;height:50px}
.review .avatar{position:absolute;left:0;top:3px;width:44px;height:44px;border-radius:50%;border:2px solid #fff;box-shadow:0 0 2px #999}
.review .card{position:absolute;left:53px;top:0;width:257px;height:50px;background:var(--white);border:1px solid #ccc;padding:6px 6px 0 30px;font-family:"Open Sans",sans-serif;font-size:8px;line-height:11px;color:#666}
.review .card::before{content:"";position:absolute;left:-7px;top:18px;width:12px;height:12px;background:#fff;border-left:1px solid #ccc;border-bottom:1px solid #ccc;transform:rotate(45deg)}
.review .card q{position:absolute;left:8px;top:2px;font-family:Georgia,serif;font-size:22px;color:#ccc;quotes:"\201C" "\201D"}
.review .card q::after{content:""}
.review .who{font-size:7.5px;margin-top:2px}
.review .who span{color:var(--blue-name)}
.review .who em{font-style:normal;color:#999}
.review-dots{left:308px;top:985px;display:flex;gap:4px}
.review-dots i{width:8px;height:8px;border-radius:50%;background:#c6d4e0;border:1px solid #9ab}
.review-dots i.on{background:#c8a048}

/* footer */
.footer{left:0;top:1010px;width:676px;height:140px;background:var(--panel)}
.footer h5{position:absolute;top:10px;font-family:var(--head-font);font-weight:400;font-size:12px;color:#999}
.footer ul{position:absolute;top:40px;list-style:none;font-size:6.5px;line-height:16px;font-weight:bold;color:#bbb}
.footer ul span{color:#777;font-weight:normal}
.footer .testimonial{position:absolute;left:358px;top:36px;width:130px;font-size:6.5px;line-height:8px;color:#888;font-weight:bold}
.footer .testimonial .sig{text-align:right;margin-top:18px;padding-right:18px}
.footer .follow{position:absolute;left:572px;top:14px;display:flex;gap:4px;align-items:center;font-size:6.5px;color:#ccc;font-family:Georgia,serif}
.footer .follow i{width:11px;height:11px;background:#444}
.footer .ghost-name{position:absolute;left:540px;top:80px;font-family:var(--head-font);font-size:18px;color:#444}
.linksbar{left:0;top:1150px;width:676px;height:24px;background:var(--panel-dark);border-top:1px solid #3a3a3a;text-align:center;font-family:Georgia,serif;font-size:7px;line-height:24px;color:#ccc}
.copyright{left:0;top:1174px;width:676px;height:26px;background:var(--black);font-size:6.5px;font-weight:bold;line-height:26px;padding-left:30px}
</style>
</head>
<body>
<div class="page">

  <div class="abs topbar">
    <div class="abs email">Email us: <span>info@tidesofbloom.com</span></div>
    <div class="abs search">
      <svg width="22" height="16" viewBox="0 0 22 16"><circle cx="10" cy="7" r="3.5" fill="none" stroke="#ccc" stroke-width="1.2"/><line x1="12.5" y1="9.5" x2="15" y2="12" stroke="#ccc" stroke-width="1.3"/></svg>
    </div>
    <div class="abs lang">English ▾</div>
  </div>

  <header class="abs header">
    <div class="abs social" style="left:593px;top:14px"><i class="blue"></i><i></i><i></i></div>
    <nav class="abs nav" style="top:46px">
      <span class="current">Home</span><span>Business</span><span>Individual</span><span>Contact</span>
    </nav>
  </header>

  <div class="abs brand"><span class="mark"></span><span class="name">Tides of Bloom</span></div>

  <section class="abs hero">
    <div class="abs hero-photo" role="img" aria-label="Photo of a smiling older couple, cheek to cheek"></div>
    <div class="abs hero-callout">
      <h1>Tides of Bloom</h1>
      <p>Improve your relationship at it source ...</p>
    </div>
  </section>
  <div class="abs hero-dots"><i class="on"></i><i></i><i></i><i></i></div>

  <div class="abs band"></div>
  <div class="abs section-bar">
    <div class="tab"></div>
    <div class="title">CHANGE IS YOURS</div>
    <div class="phone">
      <svg width="16" height="16" viewBox="0 0 16 16"><circle cx="8" cy="8" r="7" fill="none" stroke="#333" stroke-width="1.2"/><path d="M5.3 4.2l1.4-.2.8 2-1 .8c.5 1.2 1.4 2.1 2.6 2.6l.8-1 2 .8-.2 1.4c-3.6.3-6.700-2.8-6.4-6.4z" fill="#333"/></svg>
      555-555-5555
    </div>
  </div>

  <section class="abs services">
    <article class="service">
      <h3><span class="bullet"></span><span class="txt">More choices about<br>your behaviours and emotions</span></h3>
      <div class="photo" role="img" aria-label="Photo of a group of colleagues standing together" style="background:linear-gradient(135deg,#b9a79a,#6e6a6a 60%,#9a8f88)"></div>
      <p>Lorem ipsum dolor sit amet, consectetur adipiscing elit. Suspendisse molestie arcu sed adipiscing hendrerit. Fusce dignissim pellentesque augue, quis pretium urna feugiat nec. Duis fermentum pellentesque aliquam. Proin sed nunc non arcu lobortis sollicitudin. Vestibulum non ipsum commodo, congue dolor ut, volutpat tellus. Nulla quis velit id nulla sagittis egestas. In hac habitasse platea dictumst.</p>
      <span class="more">more...</span>
    </article>
    <article class="service">
      <h3><span class="bullet"></span><span class="txt">Improve your relationships<br>and the ways you communicate</span></h3>
      <div class="photo" role="img" aria-label="Photo of two people in conversation" style="background:linear-gradient(90deg,#8a7a6a,#b4aca4 50%,#7a3a6a)"></div>
      <p>Lorem ipsum dolor sit amet, consectetur adipiscing elit. Suspendisse molestie arcu sed adipiscing hendrerit. Fusce dignissim pellentesque augue, quis pretium urna feugiat nec. Duis fermentum pellentesque aliquam. Proin sed nunc non arcu lobortis sollicitudin. Vestibulum non ipsum commodo, congue dolor ut, volutpat tellus. Nulla quis velit id nulla sagittis egestas. In hac habitasse platea dictumst.</p>
      <span class="more">more...</span>
    </article>
    <article class="service">
      <h3><span class="bullet"></span><span class="txt">Create better results through<br>becoming a greater thinker</span></h3>
      <div class="photo" role="img" aria-label="Black and white photo of three older men" style="background:linear-gradient(90deg,#f2f2f2,#9a9a9a 45%,#cfcfcf 70%,#f4f4f4)"></div>
      <p>Lorem ipsum dolor sit amet, consectetur adipiscing elit. Suspendisse molestie arcu sed adipiscing hendrerit. Fusce dignissim pellentesque augue, quis pretium urna feugiat nec. Duis fermentum pellentesque aliquam. Proin sed nunc non arcu lobortis sollicitudin. Vestibulum non ipsum commodo, congue dolor ut, volutpat tellus. Nulla quis velit id nulla sagittis egestas. In hac habitasse platea dictumst.</p>
      <span class="more">more...</span>
    </article>
  </section>

  <div class="abs quote-banner"><b>“</b> LIPSUM LOREM DOLOR SIT AMET <b>”</b></div>
  <div class="abs quote-tip"></div>

  <section class="abs features">
    <div class="feature" style="top:16px">
      <div class="thumb" role="img" aria-label="Photo of glass office towers" style="background:linear-gradient(135deg,#dfe8ee,#6f8796 60%,#b8c6cf)"></div>
      <h4>LIPSUM LOREM</h4>
      <p>Not a lifelong project or<br>years of therapy.</p>
      <span class="detail">detail</span>
    </div>
    <div class="feature" style="top:94px">
      <div class="thumb" role="img" aria-label="Photo of a city building facade" style="background:linear-gradient(135deg,#d9d9d9,#777 55%,#aaa)"></div>
      <h4>LIPSUM LOREM</h4>
      <p>Change begins today with our<br>Master Practitioner</p>
      <span class="detail">detail</span>
    </div>
  </section>
  <div class="abs feature-rule"></div>
  <div class="abs feature-divider"></div>

  <section class="abs about">
    <h2>IIPSUM IOREM</h2>
    <p>Our clients experience their desired instant &amp; permanent transformation, emerging from our consultations ready to take on their world from a vastly different paradigm</p>
    <p>At Tides Of Bloom, our Master Practitioner will inspire you, shifting your perspective &amp; facilitating your mind with the freedom to realise your dreams</p>
    <p>Join Walter Brandt, Hugh Marlow, E.M. Castell, Rory Lane, Owen Price, Dana Whitcombe and hundreds of thousands of others who are achieving the life changing, consistent results you are dreaming of now.</p>
  </section>
  <div class="abs gallery">
    <figure><div class="shot" role="img" aria-label="Photo of a rocky coastline" style="background:linear-gradient(#8fb8d8,#c9b48a 60%,#7a8a5a)"></div><figcaption>Development and future project</figcaption></figure>
    <figure><div class="shot" role="img" aria-label="Photo of a tropical beach with palm trees" style="background:linear-gradient(#3d8ed0,#6fb6d9 55%,#e2d6b0)"></div><figcaption>Our high quality project</figcaption></figure>
    <figure><div class="shot" role="img" aria-label="Photo of a sunny bay landscape" style="background:linear-gradient(#9cc4e4,#4a90b8 50%,#8aa060)"></div><figcaption>Advertising and Marketing</figcaption></figure>
  </div>

  <section class="abs reviews">
    <h2>WHAT OUR CLIENT HAS TO SAY ABOUT <b>“TIDES OF BLOOM”</b> EXPERIENCE</h2>
    <div class="review" style="left:24px">
      <div class="avatar" role="img" aria-label="Client portrait photo" style="background:radial-gradient(#c9a58a,#5a4030)"></div>
      <div class="card"><q></q>Lorem ipsum dolor sit amet, consectetur adipiscing elit. Nullam ut libero et libero sagittis interdum et vitae.
        <div class="who"><span>Marla Dunn</span>, <em>Modesto</em></div></div>
    </div>
    <div class="review" style="left:348px">
      <div class="avatar" role="img" aria-label="Client portrait photo" style="background:radial-gradient(#e2c09a,#b08850)"></div>
      <div class="card"><q></q>Lorem ipsum dolor sit amet, consectetur adipiscing elit. Nullam ut libero et libero sagittis interdum et vitae.
        <div class="who"><span>Marla Dunn</span>, <em>Modesto</em></div></div>
    </div>
  </section>
  <div class="abs review-dots"><i></i><i></i><i class="on"></i><i></i><i></i></div>

  <footer class="abs footer">
    <h5 style="left:40px">Contact</h5>
    <ul style="left:42px">
      <li>Web: <span>www.tidesofbloom.biz</span></li>
      <li>Email: <span>info@tidesofbloom.com</span></li>
      <li>Phone: <span>1.800.5550199</span></li>
      <li>Fax: <span>(000) 555-010299</span></li>
      <li>Call: <span>4 555 01020 33</span></li>
    </ul>
    <h5 style="left:227px">Company</h5>
    <ul style="left:229px">
      <li>&gt; Home</li><li>&gt; Business</li><li>&gt; Individual</li><li>&gt; Info</li><li>&gt; Contact</li>
    </ul>
    <h5 style="left:357px">Testimonials</h5>
    <div class="testimonial">
      Lorem ipsum dolor sit amet, consectetur adipiscing elit. Suspendisse molestie arcu sed adipiscing hendrerit.
      <div class="sig">Evan Pryor.</div>
    </div>
    <div class="follow">We are at <i></i><i></i><i></i></div>
    <div class="ghost-name">Tides of Bloom</div>
  </footer>

  <div class="abs linksbar">Home | Business | Individual | Contact | Terms &amp; Conditions | Privacy Policy | Sitemap</div>
  <div class="abs copyright">Copyrights © 2013 TidesofBloom.com. All Rights Reserved.</div>

</div>
</body>
</html>
```